Business Card Design - Koru Lantern

We (Koru Lantern) need a business card design for our boutique mobile marketing agency based in Sydney, Australia.
We work with brands and advertisers to deliver and implement end to end mobile (smartphone and tablet) marketing solutions.

We already have a logo and website design, these files will be provided. Our colours centre around a blue/orange mix (the logo containing the orange (colour code: RGB 255,165,0).

Our name and logo communicate strength and confidence. We see ourselves as being trustworthy advisors who are also fun and passionate.

Target Market(s)

Senior Marketing Managers

Industry/Entity Type

Marketing

Requirements
Must have
• Employee Name: Mark Ellery
Mobile Number: 0491 573 862
Email Address xxxx@korulantern.example
Website: www.korulantern.example
Twitter ID: KoruLantern

```html
<!DOCTYPE html>
<html lang="en">
<head>
<meta charset="utf-8">
<title>Koru Lantern – Business Card</title>
<link rel="stylesheet" href="https://fonts.googleapis.com/css2?family=Open+Sans:wght@400;600;700&display=swap">
<style>
  :root {
    --page-bg: #ffffff;
    --orange-core: #ef7a36;
    --orange-edge: #e2401f;
    --black-top: #050505;
    --black-bottom: #2e2e2e;
    --ink-dark: #3a3330;
    --ink-muted: #414141;
    --accent-red: #e2331d;
    --white: #ffffff;
  }
  * { margin: 0; padding: 0; box-sizing: border-box; }
  html, body {
    width: 1200px;
    height: 512px;
    overflow: hidden;
    background: var(--page-bg);
    font-family: "Open Sans", Arial, sans-serif;
  }
  .canvas {
    width: 1200px;
    height: 512px;
    display: flex;
    align-items: center;
    justify-content: center;
    gap: 48px;
  }
  .card {
    width: 520px;
    height: 297px;
    position: relative;
    box-shadow: 0 10px 24px rgba(0, 0, 0, 0.18);
  }
  .card--front {
    background: radial-gradient(ellipse at 48% 45%, var(--orange-core) 0%, var(--orange-core) 20%, var(--orange-edge) 100%);
    display: flex;
    align-items: center;
    padding: 0 30px 0 44px;
  }
  .card--back {
    background: linear-gradient(to bottom, var(--black-top) 0%, var(--black-bottom) 100%);
    display: flex;
    align-items: center;
    justify-content: center;
  }
  .brand {
    display: flex;
    align-items: center;
    gap: 10px;
  }
  .brand__dot {
    width: 22px;
    height: 22px;
    border-radius: 50%;
    flex: none;
  }
  .brand__name {
    font-size: 30px;
    font-weight: 700;
    letter-spacing: 0.5px;
    white-space: nowrap;
  }
  .card--front .brand__dot { background: var(--white); }
  .card--front .brand__name { color: var(--ink-dark); }
  .card--back .brand__dot { background: var(--accent-red); }
  .card--back .brand__name { color: var(--ink-muted); }
  .divider {
    width: 1px;
    height: 132px;
    background: var(--white);
    margin: 0 22px 0 22px;
    flex: none;
  }
  .contact { color: var(--white); }
  .contact__name {
    font-size: 21px;
    font-weight: 700;
    margin-bottom: 26px;
    letter-spacing: -0.2px;
  }
  .contact__list {
    list-style: none;
    font-size: 10.5px;
    line-height: 1.45;
  }
</style>
</head>
<body>
  <main class="canvas">
    <section class="card card--front" aria-label="Business card front">
      <div class="brand">
        <span class="brand__dot"></span>
        <span class="brand__name">Koru Lantern</span>
      </div>
      <span class="divider"></span>
      <div class="contact">
        <p class="contact__name">Mark Ellery</p>
        <ul class="contact__list">
          <li>Mobile: 0491 573 862</li>
          <li>Email: info@korulantern.example</li>
          <li>Website: www.korulantern.example</li>
          <li>Twitter ID: KoruLantern</li>
        </ul>
      </div>
    </section>
    <section class="card card--back" aria-label="Business card back">
      <div class="brand">
        <span class="brand__dot"></span>
        <span class="brand__name">Koru Lantern</span>
      </div>
    </section>
  </main>
</body>
</html>
```